M Zyvantics Buisness Cards

I need a technology focused clean business card for my employees. I have attached out logo to include in the mocks. We're a modern tech consulting firm that drives to interface humanity with technology in a truly cohesive fashion.

```html
<!DOCTYPE html>
<html lang="en">
<head>
<meta charset="utf-8">
<title>M Zyvantics Business Cards</title>
<link rel="stylesheet" href="https://fonts.googleapis.com/css2?family=Montserrat:wght@600;700&family=Open+Sans:wght@400;600&display=swap">
<style>
  :root {
    --page-bg: #ececec;
    --card-bg: #231f20;
    --card-bg-soft: #2c2829;
    --brand-grey: #8e9194;
    --brand-blue: #1e73be;
    --text-light: #f2f2f2;
    --text-muted: #c9c9c9;
  }
  * { box-sizing: border-box; margin: 0; padding: 0; }
  html, body {
    width: 1200px; height: 800px; overflow: hidden;
    background: var(--page-bg);
  }
  .sheet {
    width: 1200px; height: 800px;
    display: flex; align-items: center; justify-content: center; gap: 60px;
  }
  .card {
    position: relative;
    width: 500px; height: 286px;
    border-radius: 3px;
    overflow: hidden;
    box-shadow: 0 10px 24px rgba(0,0,0,0.18);
  }
  .card-texture {
    position: absolute; inset: 0;
    background: radial-gradient(ellipse at 50% 40%, var(--card-bg-soft), var(--card-bg) 75%);
  }
  .wordmark {
    position: absolute; left: 0; right: 0;
    display: flex; align-items: center; justify-content: center; gap: 14px;
    font-family: "Montserrat", sans-serif;
    font-weight: 700;
    color: var(--brand-grey);
    letter-spacing: 0.5px;
  }
  .wordmark-dot {
    border-radius: 50%;
    background: var(--brand-blue);
  }
  .card--front .wordmark { top: 105px; font-size: 46px; }
  .card--front .wordmark-dot { width: 22px; height: 22px; }
  .card--back .wordmark { top: 50px; font-size: 36px; }
  .card--back .wordmark-dot { width: 18px; height: 18px; }
  .divider {
    position: absolute; left: 22px; right: 22px; top: 150px;
    height: 2px; background: var(--brand-blue);
  }
  .identity {
    position: absolute; left: 40px; top: 172px;
  }
  .identity-name {
    font-family: "Montserrat", sans-serif;
    font-weight: 700; font-size: 22px;
    color: var(--text-light); letter-spacing: 0.5px;
  }
  .identity-role {
    font-family: "Open Sans", sans-serif;
    font-size: 13px; color: var(--text-muted); margin-top: 2px;
  }
  .contacts {
    position: absolute; right: 50px; top: 166px;
    list-style: none;
    font-family: "Open Sans", sans-serif;
    font-size: 13px; color: var(--text-light);
  }
  .contact-item {
    display: flex; align-items: center; gap: 8px; height: 20px;
  }
  .contact-icon {
    width: 14px; height: 14px; flex: none;
  }
</style>
</head>
<body>
<main class="sheet">
  <section class="card card--front" aria-label="Card front">
    <div class="card-texture" role="img" aria-label="Dark textured card background with subtle repeating brand pattern"></div>
    <div class="wordmark"><span class="wordmark-dot"></span><span class="wordmark-name">M Zyvantics</span></div>
  </section>

  <section class="card card--back" aria-label="Card back">
    <div class="card-texture" role="img" aria-label="Dark textured card background with subtle repeating brand pattern"></div>
    <div class="wordmark"><span class="wordmark-dot"></span><span class="wordmark-name">M Zyvantics</span></div>
    <div class="divider"></div>
    <div class="identity">
      <p class="identity-name">NAME</p>
      <p class="identity-role">Designation</p>
    </div>
    <ul class="contacts">
      <li class="contact-item">
        <svg class="contact-icon" viewBox="0 0 14 14" aria-hidden="true">
          <circle cx="7" cy="7" r="7" fill="#1e73be"/>
          <path d="M4.6 3.6l1.3 1.4-.7.9c.5 1 1.2 1.7 2.1 2.2l.9-.7 1.4 1.3-.8 1.2C6.6 9.6 4.3 7.3 4 4.5z" fill="#fff"/>
        </svg>
        <span>(555) 014-2290</span>
      </li>
      <li class="contact-item">
        <svg class="contact-icon" viewBox="0 0 14 14" aria-hidden="true">
          <circle cx="7" cy="7" r="7" fill="#1e73be"/>
          <circle cx="7" cy="7" r="3.8" fill="none" stroke="#fff" stroke-width="0.9"/>
          <ellipse cx="7" cy="7" rx="1.6" ry="3.8" fill="none" stroke="#fff" stroke-width="0.8"/>
          <line x1="3.2" y1="7" x2="10.8" y2="7" stroke="#fff" stroke-width="0.8"/>
        </svg>
        <span>Website</span>
      </li>
      <li class="contact-item">
        <svg class="contact-icon" viewBox="0 0 14 14" aria-hidden="true">
          <circle cx="7" cy="7" r="7" fill="#1e73be"/>
          <rect x="3.5" y="4.5" width="7" height="5" fill="none" stroke="#fff" stroke-width="0.9"/>
          <path d="M3.5 4.7L7 7.4l3.5-2.7" fill="none" stroke="#fff" stroke-width="0.9"/>
        </svg>
        <span>Email</span>
      </li>
    </ul>
  </section>
</main>
</body>
</html>
```